Restaurant Bar website in Oakland

Landing page that looks good on mobile and home. Easy to make changes to SEO and Menu page .
Might link with online ordering through the point of sale provider or not. Either way we want to be able to upload menus.
No forms need. Just landing page, about page with a paragraph and a few photos, address, hours and a mailto info@
A press page and an faq

Target Market(s)

Customers

Coding

Coded - Design and coding required

Number of Pages Required

4 page

Colors
00a990
ffc214

Requirements
Must have
• Simple to scroll
SEO
Simple to add menus
Our logo

```html
<!DOCTYPE html>
<html lang="en">
<head>
<meta charset="utf-8">
<title>Harlow's — Restaurant &amp; Bar</title>
<link href="https://fonts.googleapis.com/css2?family=Bebas+Neue&family=Heebo:wght@400&display=swap" rel="stylesheet">
<style>
  :root {
    --gold: #ffc214;
    --logo-gold: #c9a14a;
    --white: #ffffff;
    --ink: #000000;
    --icon-ink: #111111;
    --hero-dark: #2a1608;
    --hero-warm: #7a4a1c;
    --info-bg: #0b0a08;
    --divider: rgba(255,255,255,0.45);
  }
  * { margin: 0; padding: 0; box-sizing: border-box; }
  html, body { width: 1200px; height: 1029px; overflow: hidden; background: var(--ink); }
  .page { position: relative; width: 1200px; height: 1029px; overflow: hidden; }

  .hero { position: absolute; left: 0; top: 0; width: 1200px; height: 666px; }
  .hero-photo {
    position: absolute; inset: 0;
    background:
      radial-gradient(ellipse at 30% 70%, rgba(214,140,50,0.55), transparent 55%),
      radial-gradient(ellipse at 80% 40%, rgba(120,70,30,0.5), transparent 60%),
      linear-gradient(180deg, #3a2210 0%, var(--hero-warm) 55%, var(--hero-dark) 100%);
  }
  .main-nav {
    position: absolute; top: 0; left: 0; width: 1200px; height: 150px;
    font-family: 'Bebas Neue', sans-serif; font-size: 21px; color: var(--white);
  }
  .main-nav a { position: absolute; top: 63px; transform: translateX(-50%); color: inherit; text-decoration: none; letter-spacing: 0.3px; }
  .nav-brand {
    position: absolute; left: 581px; top: 48px; transform: translateX(-50%);
    font-family: 'Bebas Neue', sans-serif; font-size: 50px; color: var(--logo-gold); letter-spacing: 3px; white-space: nowrap;
  }
  .hero-brand {
    position: absolute; left: 600px; top: 280px; transform: translateX(-50%);
    font-family: 'Bebas Neue', sans-serif; font-size: 128px; font-weight: 400; line-height: 1; color: var(--logo-gold); letter-spacing: 8px; white-space: nowrap;
  }
  .play-button { position: absolute; left: 559px; top: 499px; width: 82px; height: 82px; }

  .info { position: absolute; left: 0; top: 666px; width: 1200px; height: 289px; }
  .info-photo {
    position: absolute; inset: 0;
    background:
      radial-gradient(ellipse at 20% 90%, rgba(90,70,40,0.35), transparent 50%),
      radial-gradient(ellipse at 85% 60%, rgba(70,70,70,0.3), transparent 55%),
      linear-gradient(180deg, #1a140a 0%, var(--info-bg) 40%, #14120f 100%);
  }
  .info-item { position: absolute; top: 52px; width: 320px; transform: translateX(-50%); text-align: center; color: var(--white); }
  .info-item svg { display: block; margin: 0 auto; }
  .info-title { font-family: 'Bebas Neue', sans-serif; font-size: 26px; font-weight: 400; margin-top: 11px; line-height: 1.1; }
  .info-text { font-family: 'Heebo', sans-serif; font-size: 16px; line-height: 28px; margin-top: 3px; }
  .info-text a { color: inherit; text-decoration: none; }
  .divider { position: absolute; top: 68px; width: 1px; height: 110px; background: var(--divider); }

  .site-footer { position: absolute; left: 0; top: 955px; width: 1200px; height: 74px; background: var(--ink); }
  .copyright { position: absolute; left: 101px; top: 26px; font-family: 'Heebo', sans-serif; font-size: 16px; color: var(--white); }
  .social-links { position: absolute; top: 17px; left: 0; }
  .social-link { position: absolute; width: 40px; height: 40px; border-radius: 50%; background: var(--gold); display: flex; align-items: center; justify-content: center; }
  .social-link svg { width: 18px; height: 18px; }
</style>
</head>
<body>
<div class="page">
  <header class="hero">
    <div class="hero-photo" role="img" aria-label="Warmly lit bar interior with a long wooden counter, wine racks and bottle shelves"></div>
    <nav class="main-nav">
      <a href="#" style="left:211px">Home</a>
      <a href="#" style="left:329px">About</a>
      <a href="#" style="left:450px">Press</a>
      <div class="nav-brand">Harlow's</div>
      <a href="#" style="left:727px">Gallery</a>
      <a href="#" style="left:842px">FAQ</a>
      <a href="#" style="left:969px">Contact Us</a>
    </nav>
    <h1 class="hero-brand">Harlow's</h1>
    <svg class="play-button" viewBox="0 0 82 82" aria-label="Play video">
      <circle cx="41" cy="41" r="41" fill="rgba(255,255,255,0.85)"/>
      <circle cx="41" cy="41" r="25" fill="#ffffff"/>
      <path d="M36 33 L49 41 L36 49 Z" fill="#1e4a32"/>
    </svg>
  </header>

  <section class="info">
    <div class="info-photo" role="img" aria-label="Dimly lit back bar with glassware and bottles"></div>

    <div class="info-item" style="left:232px">
      <svg width="82" height="82" viewBox="0 0 82 82" fill="none" stroke="#ffc214" stroke-width="3">
        <rect x="2" y="24" width="78" height="36"/>
        <path d="M26 52 A15 15 0 0 1 56 52 Z"/>
        <line x1="22" y1="52" x2="60" y2="52"/>
        <line x1="41" y1="34" x2="41" y2="37"/>
        <line x1="41" y1="60" x2="41" y2="74"/>
        <path d="M28 79 L54 79 L48 74 L34 74 Z"/>
        <path d="M2 2 L2 14 L24 14 L32 20"/>
      </svg>
      <h2 class="info-title">Contact Us</h2>
      <p class="info-text"><a href="mailto:info@harlows.com">info@harlows.com</a></p>
    </div>

    <div class="divider" style="left:390px"></div>

    <div class="info-item" style="left:547px">
      <svg width="82" height="82" viewBox="0 0 82 82" fill="none" stroke="#ffc214" stroke-width="3">
        <circle cx="41" cy="41" r="32"/>
        <circle cx="41" cy="41" r="28"/>
        <line x1="41" y1="41" x2="28" y2="26"/>
        <line x1="41" y1="41" x2="62" y2="41"/>
      </svg>
      <h2 class="info-title">Open Hours</h2>
      <p class="info-text">Temporarily Closed</p>
    </div>

    <div class="divider" style="left:703px"></div>

    <div class="info-item" style="left:914px">
      <svg width="82" height="82" viewBox="0 0 82 82" fill="none" stroke="#ffc214" stroke-width="3">
        <path d="M41 66 C28 50 19 38 19 26 A22 22 0 0 1 63 26 C63 38 54 50 41 66 Z"/>
        <circle cx="41" cy="25" r="9"/>
        <path d="M24 58 L12 58 L2 80 L80 80 L70 58 L58 58"/>
      </svg>
      <h2 class="info-title">Address</h2>
      <p class="info-text">4821 Telegraph Lane Oakland CA<br>94609 &nbsp;| 510 555 0147</p>
    </div>
  </section>

  <footer class="site-footer">
    <p class="copyright">© 2021 Harlow's. All Rights Reserved.</p>
    <div class="social-links">
      <a class="social-link" href="#" aria-label="Social profile 1" style="left:909px">
        <svg viewBox="0 0 18 18" fill="none" stroke="#111111" stroke-width="2" stroke-linecap="round"><path d="M4 14 L14 4 M7 4 H14 V11"/></svg>
      </a>
      <a class="social-link" href="#" aria-label="Social profile 2" style="left:959px">
        <svg viewBox="0 0 18 18" fill="none" stroke="#111111" stroke-width="2" stroke-linecap="round"><path d="M4 14 L14 4 M7 4 H14 V11"/></svg>
      </a>
      <a class="social-link" href="#" aria-label="Social profile 3" style="left:1007px">
        <svg viewBox="0 0 18 18" fill="none" stroke="#111111" stroke-width="2" stroke-linecap="round"><path d="M4 14 L14 4 M7 4 H14 V11"/></svg>
      </a>
      <a class="social-link" href="#" aria-label="Social profile 4" style="left:1057px">
        <svg viewBox="0 0 18 18" fill="none" stroke="#111111" stroke-width="2" stroke-linecap="round"><path d="M4 14 L14 4 M7 4 H14 V11"/></svg>
      </a>
    </div>
  </footer>
</div>
</body>
</html>
```